The Lantern Guide

I am a life coach specializing in helping people with depression and bipolar disorder. I would like a nice, fun design for a business card.

```html
<!DOCTYPE html>
<html lang="en">
<head>
<meta charset="utf-8">
<title>The Lantern Guide – Business Card</title>
<link rel="stylesheet" href="https://fonts.googleapis.com/css2?family=Open+Sans:wght@300;400;700&display=swap">
<style>
  :root {
    --backdrop: #2a2a2c;
    --card: #121213;
    --green: #7db227;
    --red: #e02020;
    --orange: #f5a31a;
    --white: #ffffff;
    --muted: #e6e6e6;
    --icon-blue: #0b3f8c;
    --icon-sky: #1b8fe0;
    --icon-navy: #2a3f75;
  }
  * { box-sizing: border-box; margin: 0; padding: 0; }
  html, body { width: 1200px; height: 1003px; overflow: hidden; }
  body {
    background: var(--backdrop);
    font-family: "Open Sans", sans-serif;
    display: flex; align-items: center; justify-content: center;
  }
  .card {
    position: relative;
    width: 1100px; height: 630px;
    background: var(--card);
    border-radius: 18px;
    overflow: hidden;
    color: var(--white);
  }
  .card-shapes { position: absolute; inset: 0; }
  .brand-mark {
    position: absolute; left: 110px; top: 95px; width: 220px;
    text-align: center; font-weight: 700; font-size: 30px; line-height: 1.15;
    color: var(--white);
  }
  .identity { position: absolute; left: 70px; top: 360px; }
  .identity-name {
    font-weight: 700; font-size: 40px; letter-spacing: 0.5px;
    text-transform: uppercase; line-height: 1.1;
  }
  .identity-tagline { font-weight: 300; font-size: 27px; color: var(--muted); }
  .logo-placeholder {
    position: absolute; right: 90px; top: 150px;
    font-weight: 300; font-size: 28px; line-height: 1.15; color: var(--muted);
  }
  .contacts {
    position: absolute; left: 560px; top: 330px; list-style: none;
  }
  .contact {
    display: flex; align-items: center; gap: 26px;
    height: 52px; font-weight: 300; font-size: 30px; color: var(--muted);
  }
  .contact-phone-number { font-weight: 400; font-size: 34px; color: var(--white); }
  .contact-icon { width: 40px; height: 40px; flex: none; }
</style>
</head>
<body>
  <main class="card">
    <svg class="card-shapes" width="1100" height="630" viewBox="0 0 1100 630" aria-hidden="true">
      <polygon points="50,0 380,0 400,330 0,190" fill="var(--green)"/>
      <polyline points="75,235 40,300 70,345" fill="none" stroke="var(--green)" stroke-width="2"/>
      <polygon points="560,0 620,0 585,40" fill="var(--red)"/>
      <polygon points="720,630 790,630 770,585" fill="var(--red)"/>
      <polygon points="0,440 22,440 0,480" fill="var(--orange)"/>
      <path d="M1045,0 Q1100,40 1100,110 L1100,0 Z" fill="var(--white)"/>
    </svg>

    <div class="brand-mark">The Lantern Guide</div>

    <header class="identity">
      <h1 class="identity-name">The Lantern Guide</h1>
      <p class="identity-tagline">helping people</p>
    </header>

    <p class="logo-placeholder">Company Logo<br>Placed Here</p>

    <ul class="contacts">
      <li class="contact">
        <svg class="contact-icon" viewBox="0 0 40 40" aria-label="Phone">
          <circle cx="20" cy="20" r="19" fill="var(--white)"/>
          <path d="M15 10 l4 1 -1 6 -2 1 q1 5 5 8 l2 -1 5 2 -1 4 q-9 1 -14 -8 q-3 -7 2 -13z" fill="var(--icon-blue)"/>
        </svg>
        <span class="contact-phone-number">0555 01234567</span>
      </li>
      <li class="contact">
        <svg class="contact-icon" viewBox="0 0 40 40" aria-label="Email">
          <circle cx="20" cy="20" r="19" fill="var(--red)"/>
          <rect x="9" y="13" width="22" height="15" fill="var(--white)"/>
          <polyline points="9,13 20,22 31,13" fill="none" stroke="var(--red)" stroke-width="2"/>
        </svg>
        <span>www.lantern-guide.</span>
      </li>
      <li class="contact">
        <svg class="contact-icon" viewBox="0 0 40 40" aria-hidden="true"><circle cx="20" cy="20" r="19" fill="var(--icon-sky)"/></svg>
        <span>office@lantern-guide.</span>
      </li>
      <li class="contact">
        <svg class="contact-icon" viewBox="0 0 40 40" aria-hidden="true"><circle cx="20" cy="20" r="19" fill="var(--icon-navy)"/></svg>
        <span>office@lantern-guide.</span>
      </li>
      <li class="contact">
        <svg class="contact-icon" viewBox="0 0 40 40" aria-label="Address">
          <circle cx="20" cy="20" r="19" fill="var(--white)"/>
          <path d="M20 8 a8 8 0 0 1 8 8 c0 6 -8 15 -8 15 s-8 -9 -8 -15 a8 8 0 0 1 8 -8z" fill="var(--icon-blue)"/>
          <circle cx="20" cy="16" r="3" fill="var(--white)"/>
        </svg>
        <span>company address</span>
      </li>
    </ul>
  </main>
</body>
</html>
```